Quellin Rebranded Website boutique fitness studio

Looking for a simple, easy to navigate, aesthetically pleasing update of our rebranded website

Target Market(s)

Stay at home moms, discretionary income, fitness and wellness

Coding

Coded - Design and coding required

Number of Pages Required

1 page

Font styles to use
Sans Serif

Colors
0054AA
0677BA
7BADD7
CADEEF
E8F1F8

Requirements
Must have
• Instagram feed linked, "as seen in" banner, spot for studio video at a later date

```html
<!DOCTYPE html>
<html lang="en">
<head>
<meta charset="utf-8">
<title>Quellin — Boutique Kinetra Studio</title>
<link href="https://fonts.googleapis.com/css2?family=Albert+Sans:wght@400;500;600;700&display=swap" rel="stylesheet">
<style>
:root{
  --navy:#1c2b4b;
  --navy-deep:#15213b;
  --navy-soft:#2a3b5f;
  --sand:#d8c6b0;
  --sand-light:#efe6dd;
  --ink:#1f2533;
  --muted:#6b7180;
  --accent:#8c4a3b;
  --line:#e4e6ea;
  --tick:#3aa35a;
  --star:#f2b418;
  --white:#ffffff;
  --card-tint:#f3ece6;
  --card-grey:#e6e8ec;
}
*{box-sizing:border-box;margin:0;padding:0}
html,body{width:1200px;height:5319px;overflow:hidden}
body{position:relative;background:var(--white);font-family:"Albert Sans",Helvetica,Arial,sans-serif;color:var(--ink)}
.abs{position:absolute}
.photo{position:absolute;overflow:hidden}
.btn{display:inline-flex;align-items:center;gap:10px;background:var(--sand);color:var(--ink);font-size:11px;font-weight:500;padding:0 24px;height:36px;border-radius:3px}
.btn svg{width:14px;height:10px}
.eyebrow{font-size:10px;letter-spacing:2px;font-weight:600;color:var(--accent);text-transform:uppercase}

/* hero */
.hero{left:12px;top:12px;width:1176px;height:680px;background:linear-gradient(100deg,#1b2947 0%,#25365a 45%,#3b4a63 70%,#2a3856 100%);overflow:hidden}
.nav{left:147px;top:23px;width:874px;height:52px;background:rgba(255,255,255,.08);border-radius:3px;display:flex;align-items:center;justify-content:space-between;padding:0 0 0 32px}
.nav-links{display:flex;gap:30px;font-size:11px;color:var(--white)}
.brand{position:absolute;left:50%;transform:translateX(-50%);display:flex;flex-direction:column;align-items:center;color:var(--white)}
.brand b{font-size:20px;font-weight:600;letter-spacing:1px}
.brand span{font-size:5px;letter-spacing:1.5px}
.nav .btn{margin-right:0;height:40px}
.hero h1{left:147px;top:240px;font-size:41px;font-weight:500;line-height:50px;color:var(--white);letter-spacing:-.3px}
.hero p.lead{left:147px;top:358px;width:420px;font-size:11px;line-height:20px;color:#e5e8ef}
.hero .ctas{left:147px;top:424px;display:flex;align-items:center;gap:32px}
.link-arrow{color:var(--white);font-size:11px;display:flex;gap:12px;align-items:center}
.link-arrow u{text-underline-offset:3px}
.features{left:147px;top:592px;width:880px;display:flex;justify-content:space-between}
.feature{display:flex;align-items:center;gap:12px;color:var(--white);font-size:10px;line-height:14px}
.feature svg{width:34px;height:34px;stroke:var(--white);fill:none;stroke-width:1.4}

/* as seen */
.seen-title{top:762px;left:0;width:1200px;text-align:center;font-size:13px;color:var(--ink)}
.seen-row{top:800px;left:155px;width:890px;display:flex;justify-content:space-between;align-items:center}
.seen-row div{display:flex;align-items:center;gap:8px;font-size:20px;font-weight:500;color:#9aa0ab}
.seen-row i{display:block;width:18px;height:18px;border-radius:50%;background:#b5bac3}

/* promo */
.promo{left:12px;top:905px;width:1176px;height:293px;background:linear-gradient(90deg,#2a3a5c 0%,#1e2d4c 30%,#1a2846 100%);overflow:hidden}
.promo h2{left:205px;top:64px;font-size:26px;font-weight:500;color:var(--white)}
.promo .limited{left:205px;top:104px;font-size:10px;letter-spacing:3px;color:#c9ceda}
.bullets{left:205px;top:133px;width:420px;display:grid;grid-template-columns:1fr 1fr;row-gap:14px;font-size:10.5px;color:#e6e9f0}
.bullets span{display:flex;align-items:center;gap:8px}
.bullets i{width:9px;height:9px;border-radius:50%;background:#e6e9f0;display:block}
.promo .btn{left:205px;top:202px;position:absolute}
.countdown{left:670px;top:103px;width:361px;height:76px;display:flex;background:rgba(255,255,255,.08);border-radius:3px}
.countdown div{flex:1;display:flex;flex-direction:column;align-items:center;justify-content:center;color:var(--white);border-left:1px solid rgba(255,255,255,.12)}
.countdown div:first-child{border-left:0}
.countdown b{font-size:26px;font-weight:500}
.countdown small{font-size:8px;letter-spacing:1px;color:#aab2c4}

/* about */
.about-label{left:159px;top:1272px}
.about-img{left:159px;top:1334px;width:353px;height:378px;background:linear-gradient(180deg,#1a2c6a 0%,#3f4fa0 45%,#2b3660 100%);border-radius:3px}
.about-img span{position:absolute;left:0;right:0;bottom:28px;text-align:center;color:#d9dcef;font-size:26px;font-weight:600;letter-spacing:3px}
.about h2{left:564px;top:1266px;font-size:34px;font-weight:500;line-height:42px}
.about-col{top:1364px;width:215px;font-size:10px;line-height:21px;color:var(--muted)}
.about .btn{left:564px;top:1491px;position:absolute}
.pillars{left:564px;top:1592px;width:480px;display:flex;border-top:1px solid var(--line);border-bottom:1px solid var(--line)}
.pillars div{flex:1;display:flex;flex-direction:column;align-items:center;gap:10px;padding:14px 0 12px;font-size:10px;color:var(--ink);border-left:1px solid var(--line)}
.pillars div:first-child{border-left:0;align-items:flex-start}
.pillars svg{width:26px;height:26px;fill:none;stroke:var(--ink);stroke-width:1.4}

/* gallery */
.center-label{left:0;width:1200px;text-align:center}
.section-title{font-size:33px;font-weight:500;color:var(--ink)}
.dots{top:2677px;left:565px;display:flex;gap:6px;align-items:center}
.dots i{display:block;width:6px;height:6px;border-radius:50%;background:#c9d3e6}
.dots i.on{width:16px;border-radius:3px;background:#2e6bd0}

/* testimonials */
.reviews{left:12px;top:2759px;width:1176px;height:595px;background:var(--navy);overflow:hidden}
.reviews .eyebrow{color:#d9dde6;left:147px;top:76px;position:absolute}
.reviews h2{left:552px;top:68px;font-size:33px;font-weight:500;line-height:42px;color:var(--white);position:absolute}
.rcard{top:202px;width:281px;height:316px;background:var(--white);border-radius:3px;padding:28px 20px 20px}
.rhead{display:flex;align-items:center;gap:10px}
.avatar{width:38px;height:38px;border-radius:50%;background:linear-gradient(135deg,#c9a98f,#7d6453)}
.rhead b{font-size:12px;font-weight:600;display:block}
.rhead small{font-size:8px;color:var(--muted)}
.badge{position:absolute;right:20px;top:34px;width:16px;height:16px;border-radius:3px;background:#e3e7f0}
.rcard p{margin-top:26px;font-size:10px;line-height:20px;color:var(--ink)}
.rfoot{position:absolute;left:20px;right:20px;bottom:18px;display:flex;justify-content:space-between;align-items:center;font-size:8px;color:var(--muted)}
.stars{display:flex;gap:2px}
.stars svg{width:11px;height:11px;fill:var(--star)}
.video{background:linear-gradient(180deg,#1c2747 0%,#3a4a78 50%,#1b2440 100%);padding:24px 18px}
.video .rhead b,.video .rhead small{color:var(--white)}
.play{position:absolute;left:50%;top:50%;width:44px;height:44px;margin:-22px 0 0 -22px;border-radius:50%;background:var(--white);display:flex;align-items:center;justify-content:center}
.video .rfoot{color:var(--white)}

/* pricing */
.plan{top:3537px;width:277px;height:434px;border:1px solid var(--line);border-radius:3px;background:var(--white)}
.plan-top{height:135px;padding:30px 24px 0}
.plan-top .eyebrow{font-size:9px}
.price{margin-top:12px;font-size:36px;font-weight:500;color:var(--ink)}
.price small{font-size:20px;color:var(--muted);font-weight:400}
.plan-top p{margin-top:8px;font-size:10px;color:var(--muted)}
.plan-body{padding:24px 24px 0}
.plan-body h4{font-size:9px;letter-spacing:1.5px;color:var(--accent);font-weight:600;margin-bottom:16px}
.plan-body li{list-style:none;display:flex;align-items:center;gap:8px;font-size:11px;color:var(--ink);margin-bottom:16px}
.plan-body li svg{width:13px;height:13px}
.plan .btn{margin-top:20px;height:36px;background:var(--sand-light)}
.plan small.terms{display:block;margin-top:22px;font-size:9px;color:var(--muted)}

/* instagram */
.handle{left:564px;top:4099px;height:37px;padding:0 22px;border:1px solid #b7bcc6;border-radius:20px;display:flex;align-items:center;font-size:12px}

/* cta */
.cta{left:12px;top:4489px;width:1176px;height:304px;background:var(--navy);text-align:center;color:var(--white)}
.cta h2{margin-top:74px;font-size:33px;font-weight:500}
.cta p{margin:20px auto 0;width:380px;font-size:10.5px;line-height:20px;color:#c9cfdc}
.cta .btn{margin-top:26px;height:34px}

/* footer */
.footer{left:12px;top:4807px;width:1176px;height:498px;background:var(--navy-deep);color:var(--white)}
.footer .flogo{left:147px;top:76px;display:flex;align-items:center;gap:12px}
.footer .flogo i{display:block;width:22px;height:22px;border-radius:50%;background:var(--white)}
.footer .flogo b{font-size:40px;font-weight:600;letter-spacing:1px}
.footer .tag{left:147px;top:166px;font-size:9px;letter-spacing:1.5px}
.fcol h5{font-size:14px;font-weight:500;margin-bottom:20px}
.fcol a{display:block;font-size:8px;letter-spacing:.5px;color:#c8cedb;margin-bottom:19px;text-decoration:none;text-transform:uppercase}
.help{font-size:8px;color:#c8cedb;line-height:12px}
.help b{display:block;color:var(--white);font-size:11px;font-weight:400;margin-bottom:14px}
.socials{left:147px;top:262px;display:flex;gap:12px;align-items:center}
.socials i{display:block;width:28px;height:28px;border-radius:50%;background:var(--sand)}
.socials em{display:block;width:10px;height:10px;border-radius:50%;background:var(--white)}
.email-input{left:147px;top:386px;width:290px;height:38px;border:1px solid #3a4766;border-radius:3px;font-size:10px;color:#9aa3b8;padding:12px 18px}
.fbtn{top:386px;height:38px;background:var(--sand);color:var(--ink);font-size:10px;border-radius:3px;display:flex;align-items:center;justify-content:center;gap:10px}
.fbtn svg{width:13px;height:10px}
.fbottom{left:147px;top:465px;width:896px;display:flex;justify-content:space-between;font-size:8px;color:#aeb6c8;border-top:1px solid #2c3856;padding-top:8px}
</style>
</head>
<body>

<!-- HERO -->
<section class="hero abs">
  <div class="photo" style="inset:0;background:linear-gradient(100deg,rgba(20,32,60,.95) 0%,rgba(28,42,72,.8) 40%,rgba(70,84,104,.7) 62%,rgba(32,45,74,.9) 100%)" role="img" aria-label="Woman working out on a Kinetra machine in a dim blue-lit studio"></div>
  <nav class="nav abs">
    <div class="nav-links"><span>My Account</span><span>Buy</span><span>Policies</span></div>
    <div class="brand"><b>Quellin</b><span>ELEVATED STRENGTH</span></div>
    <span class="btn">Schedule <svg viewBox="0 0 14 10"><path d="M0 5h12M8 1l4 4-4 4" stroke="#1f2533" fill="none" stroke-width="1.3"/></svg></span>
  </nav>
  <h1 class="abs">Stronger Body.<br>Stronger Confidence.</h1>
  <p class="lead abs">Experience the transformative power of Kinetra in a welcoming, boutique studio designed for every fitness level.</p>
  <div class="ctas abs">
    <span class="btn">Claim New Client Offer <svg viewBox="0 0 14 10"><path d="M0 5h12M8 1l4 4-4 4" stroke="#1f2533" fill="none" stroke-width="1.3"/></svg></span>
    <span class="link-arrow"><u>View Class Schedule</u> <svg width="14" height="10" viewBox="0 0 14 10"><path d="M0 5h12M8 1l4 4-4 4" stroke="#fff" fill="none" stroke-width="1.3"/></svg></span>
  </div>
  <div class="features abs">
    <div class="feature"><svg viewBox="0 0 34 34"><path d="M4 30h26M7 30V12h6v18M14 30V8h6v22M21 30V16h6v14"/></svg>Low Impact, High<br>Intensity</div>
    <div class="feature"><svg viewBox="0 0 34 34"><circle cx="17" cy="7" r="3"/><path d="M10 30l5-10 4 4 4-8M8 16l8-4 6 2"/></svg>45-Minute Full Body<br>Workout</div>
    <div class="feature"><svg viewBox="0 0 34 34"><circle cx="17" cy="8" r="4"/><path d="M11 30V18a6 6 0 0 1 12 0v12"/></svg>Small Group Coaching</div>
    <div class="feature"><svg viewBox="0 0 34 34"><circle cx="10" cy="10" r="3"/><circle cx="24" cy="10" r="3"/><circle cx="17" cy="16" r="3"/><path d="M4 28c0-5 3-8 6-8M30 28c0-5-3-8-6-8M11 30c0-5 3-8 6-8s6 3 6 8"/></svg>Results You'll Feel<br>Quickly</div>
  </div>
</section>

<!-- AS SEEN IN -->
<div class="seen-title abs">As Seen In</div>
<div class="seen-row abs">
  <div><i></i>Northwell</div>
  <div><i></i>Brightside</div>
  <div><i></i>Veranda</div>
  <div><i></i>Morrow</div>
  <div><i></i>Halcyon</div>
</div>

<!-- PROMO -->
<section class="promo abs">
  <div class="photo" style="left:0;top:0;width:300px;height:293px;background:linear-gradient(90deg,#56637d 0%,#2a3a5c 100%);opacity:.7" role="img" aria-label="Client resting between sets in the studio"></div>
  <h2 class="abs">Your Strongest Start Begins Here</h2>
  <div class="limited abs">LIMITED TIME ONLY!</div>
  <div class="bullets abs">
    <span><i></i>Valid for 14 days</span><span><i></i>New clients only</span>
    <span><i></i>All classes included</span><span><i></i>Begin your Kinetra journey today</span>
  </div>
  <span class="btn">Claim Offer <svg viewBox="0 0 14 10"><path d="M0 5h12M8 1l4 4-4 4" stroke="#1f2533" fill="none" stroke-width="1.3"/></svg></span>
  <div class="countdown abs">
    <div><b>06</b><small>DAYS</small></div>
    <div><b>14</b><small>HRS</small></div>
    <div><b>32</b><small>MIN</small></div>
    <div><b>48</b><small>SEC</small></div>
  </div>
</section>

<!-- ABOUT -->
<section class="about">
  <div class="eyebrow abs about-label">What is Kinetra?</div>
  <div class="photo about-img" role="img" aria-label="Instructor demonstrating on an Arcformer under blue studio lights"><span>KINETRA</span></div>
  <h2 class="abs">Discover the<br>Power of Kinetra</h2>
  <p class="about-col abs" style="left:564px">Kinetra is a high-intensity, low-impact fitness method that combines strength, endurance, balance, and core training into one efficient full-body workout.</p>
  <p class="about-col abs" style="left:820px">Using the Arcformer, every session is designed to challenge your muscles, improve posture, and deliver lasting results while being gentle on your joints.</p>
  <span class="btn">Know More <svg viewBox="0 0 14 10"><path d="M0 5h12M8 1l4 4-4 4" stroke="#1f2533" fill="none" stroke-width="1.3"/></svg></span>
  <div class="pillars abs">
    <div><svg viewBox="0 0 26 26"><path d="M3 13h20M6 8v10M20 8v10M3 10v6M23 10v6"/></svg>Strength</div>
    <div><svg viewBox="0 0 26 26"><path d="M13 3l8 3v7c0 5-4 8-8 10-4-2-8-5-8-10V6z"/></svg>Endurance</div>
    <div><svg viewBox="0 0 26 26"><circle cx="14" cy="5" r="2.5"/><path d="M6 23l5-8 4 3 2-6M9 11l5-2 4 4"/></svg>Core</div>
    <div><svg viewBox="0 0 26 26"><circle cx="13" cy="5" r="2.5"/><path d="M5 10h16M13 10v7l-4 6M13 17l4 6"/></svg>Flexibility</div>
    <div><svg viewBox="0 0 26 26"><path d="M8 4v10a5 5 0 0 0 10 0M18 4v6M15 22h6"/></svg>Low Impact</div>
  </div>
</section>

<!-- GALLERY -->
<div class="eyebrow abs center-label" style="top:1784px">Studio Gallery</div>
<h2 class="section-title abs center-label" style="top:1812px">Inside Our Studio</h2>
<div class="photo" style="left:23px;top:1906px;width:506px;height:347px;background:linear-gradient(135deg,#3a4f9a,#5a6fb8 50%,#2a3770)" role="img" aria-label="Promo graphic of members training on Arcformers for the summer workout"></div>
<div class="photo" style="left:553px;top:1906px;width:281px;height:347px;background:linear-gradient(160deg,#1d2a5a,#354a8f 60%,#1b2348)" role="img" aria-label="Member stretching across an Arcformer"></div>
<div class="photo" style="left:859px;top:1906px;width:341px;height:347px;background:linear-gradient(135deg,#2a3568,#5163a8 50%,#1e2750)" role="img" aria-label="Member working out beside the machine"></div>
<div class="photo" style="left:0;top:2280px;width:37px;height:347px;background:linear-gradient(180deg,#2b3a78,#4a5ea6)" role="img" aria-label="Studio interior"></div>
<div class="photo" style="left:62px;top:2280px;width:281px;height:347px;background:linear-gradient(170deg,#2c3a7a,#3e4f9a 50%,#1b2248)" role="img" aria-label="Instructor coaching on the studio floor"></div>
<div class="photo" style="left:368px;top:2280px;width:505px;height:347px;background:linear-gradient(180deg,#3c4b86,#6a6ea0 55%,#2a2f4e)" role="img" aria-label="Group of instructors posing for a playlist promo"></div>
<div class="photo" style="left:898px;top:2280px;width:279px;height:347px;background:linear-gradient(180deg,#8a8c9e,#5d6f6a 60%,#2d3336)" role="img" aria-label="Three members posing together after class"></div>
<div class="dots abs"><i></i><i class="on"></i><i></i><i></i><i></i></div>

<!-- TESTIMONIALS -->
<section class="reviews abs">
  <div class="eyebrow">Results &amp; Testimonials</div>
  <h2>Real Results.<br>Real Stories.</h2>
  <article class="rcard abs" style="left:147px">
    <div class="rhead"><div class="avatar" role="img" aria-label="Client portrait"></div><div><b>Maren T.</b><small>Trusted Client</small></div></div>
    <i class="badge"></i>
    <p>"I've never felt stronger. Every class challenges me, and the coaches are incredibly supportive."</p>
    <div class="rfoot"><div class="stars"><svg viewBox="0 0 10 10"><path d="M5 0l1.5 3.2 3.5.4-2.6 2.4.7 3.5L5 7.8 1.9 9.5l.7-3.5L0 3.6l3.5-.4z"/></svg><svg viewBox="0 0 10 10"><path d="M5 0l1.5 3.2 3.5.4-2.6 2.4.7 3.5L5 7.8 1.9 9.5l.7-3.5L0 3.6l3.5-.4z"/></svg><svg viewBox="0 0 10 10"><path d="M5 0l1.5 3.2 3.5.4-2.6 2.4.7 3.5L5 7.8 1.9 9.5l.7-3.5L0 3.6l3.5-.4z"/></svg><svg viewBox="0 0 10 10"><path d="M5 0l1.5 3.2 3.5.4-2.6 2.4.7 3.5L5 7.8 1.9 9.5l.7-3.5L0 3.6l3.5-.4z"/></svg><svg viewBox="0 0 10 10"><path d="M5 0l1.5 3.2 3.5.4-2.6 2.4.7 3.5L5 7.8 1.9 9.5l.7-3.5L0 3.6l3.5-.4z"/></svg></div><span>23 May, 2026</span></div>
  </article>
  <article class="rcard video abs" style="left:446px" role="img" aria-label="Studio video testimonial placeholder">
    <div class="rhead"><div><b>Dana Whitlock</b><small>Trusted Client</small></div></div>
    <i class="badge"></i>
    <div class="play"><svg width="12" height="14" viewBox="0 0 12 14"><path d="M0 0l12 7-12 7z" fill="#1c2b4b"/></svg></div>
    <div class="rfoot"><div class="stars"><svg viewBox="0 0 10 10"><path d="M5 0l1.5 3.2 3.5.4-2.6 2.4.7 3.5L5 7.8 1.9 9.5l.7-3.5L0 3.6l3.5-.4z"/></svg><svg viewBox="0 0 10 10"><path d="M5 0l1.5 3.2 3.5.4-2.6 2.4.7 3.5L5 7.8 1.9 9.5l.7-3.5L0 3.6l3.5-.4z"/></svg><svg viewBox="0 0 10 10"><path d="M5 0l1.5 3.2 3.5.4-2.6 2.4.7 3.5L5 7.8 1.9 9.5l.7-3.5L0 3.6l3.5-.4z"/></svg><svg viewBox="0 0 10 10"><path d="M5 0l1.5 3.2 3.5.4-2.6 2.4.7 3.5L5 7.8 1.9 9.5l.7-3.5L0 3.6l3.5-.4z"/></svg><svg viewBox="0 0 10 10"><path d="M5 0l1.5 3.2 3.5.4-2.6 2.4.7 3.5L5 7.8 1.9 9.5l.7-3.5L0 3.6l3.5-.4z"/></svg></div><span>23 May, 2026</span></div>
  </article>
  <article class="rcard abs" style="left:746px">
    <div class="rhead"><div class="avatar" role="img" aria-label="Client portrait"></div><div><b>Corinne P.</b><small>Trusted Client</small></div></div>
    <i class="badge"></i>
    <p>"The welcoming community keeps me motivated. I actually look forward to every class."</p>
    <div class="rfoot"><div class="stars"><svg viewBox="0 0 10 10"><path d="M5 0l1.5 3.2 3.5.4-2.6 2.4.7 3.5L5 7.8 1.9 9.5l.7-3.5L0 3.6l3.5-.4z"/></svg><svg viewBox="0 0 10 10"><path d="M5 0l1.5 3.2 3.5.4-2.6 2.4.7 3.5L5 7.8 1.9 9.5l.7-3.5L0 3.6l3.5-.4z"/></svg><svg viewBox="0 0 10 10"><path d="M5 0l1.5 3.2 3.5.4-2.6 2.4.7 3.5L5 7.8 1.9 9.5l.7-3.5L0 3.6l3.5-.4z"/></svg><svg viewBox="0 0 10 10"><path d="M5 0l1.5 3.2 3.5.4-2.6 2.4.7 3.5L5 7.8 1.9 9.5l.7-3.5L0 3.6l3.5-.4z"/></svg><svg viewBox="0 0 10 10"><path d="M5 0l1.5 3.2 3.5.4-2.6 2.4.7 3.5L5 7.8 1.9 9.5l.7-3.5L0 3.6l3.5-.4z"/></svg></div><span>23 May, 2026</span></div>
  </article>
  <article class="rcard abs" style="left:1047px">
    <div class="rhead"><div class="avatar" role="img" aria-label="Client portrait"></div><div><b>Talia B.</b><small>Trusted Client</small></div></div>
    <p>"Low-impact but incredibly effective. My posture, strength, and confidence have completely improved."</p>
    <div class="rfoot"><div class="stars"><svg viewBox="0 0 10 10"><path d="M5 0l1.5 3.2 3.5.4-2.6 2.4.7 3.5L5 7.8 1.9 9.5l.7-3.5L0 3.6l3.5-.4z"/></svg><svg viewBox="0 0 10 10"><path d="M5 0l1.5 3.2 3.5.4-2.6 2.4.7 3.5L5 7.8 1.9 9.5l.7-3.5L0 3.6l3.5-.4z"/></svg><svg viewBox="0 0 10 10"><path d="M5 0l1.5 3.2 3.5.4-2.6 2.4.7 3.5L5 7.8 1.9 9.5l.7-3.5L0 3.6l3.5-.4z"/></svg><svg viewBox="0 0 10 10"><path d="M5 0l1.5 3.2 3.5.4-2.6 2.4.7 3.5L5 7.8 1.9 9.5l.7-3.5L0 3.6l3.5-.4z"/></svg><svg viewBox="0 0 10 10"><path d="M5 0l1.5 3.2 3.5.4-2.6 2.4.7 3.5L5 7.8 1.9 9.5l.7-3.5L0 3.6l3.5-.4z"/></svg></div></div>
  </article>
</section>

<!-- PRICING -->
<div class="eyebrow abs center-label" style="top:3426px">Pricing</div>
<h2 class="section-title abs center-label" style="top:3453px">Pricing Plans, For healthy fitness journey</h2>

<article class="plan abs" style="left:159px">
  <div class="plan-top" style="background:var(--card-tint)"><div class="eyebrow">Basic Package</div><div class="price">$50<small>/m</small></div><p>Free trial class for all new members.</p></div>
  <div class="plan-body"><h4>WHAT'S INCLUDED?</h4><ul>
    <li><svg viewBox="0 0 13 13"><circle cx="6.5" cy="6.5" r="6.5" fill="#3aa35a"/><path d="M3.5 6.7l2 2 4-4" stroke="#fff" fill="none" stroke-width="1.4"/></svg>Free Consultation</li>
    <li><svg viewBox="0 0 13 13"><circle cx="6.5" cy="6.5" r="6.5" fill="#3aa35a"/><path d="M3.5 6.7l2 2 4-4" stroke="#fff" fill="none" stroke-width="1.4"/></svg>Functional Training</li>
    <li><svg viewBox="0 0 13 13"><circle cx="6.5" cy="6.5" r="6.5" fill="#3aa35a"/><path d="M3.5 6.7l2 2 4-4" stroke="#fff" fill="none" stroke-width="1.4"/></svg>Nutrition Program</li>
    <li><svg viewBox="0 0 13 13"><circle cx="6.5" cy="6.5" r="6.5" fill="#3aa35a"/><path d="M3.5 6.7l2 2 4-4" stroke="#fff" fill="none" stroke-width="1.4"/></svg>24/7 Full Support</li></ul>
    <span class="btn">Join Now <svg viewBox="0 0 14 10"><path d="M0 5h12M8 1l4 4-4 4" stroke="#1f2533" fill="none" stroke-width="1.3"/></svg></span>
    <small class="terms">*Terms and Conditions apply</small></div>
</article>
<article class="plan abs" style="left:458px">
  <div class="plan-top" style="background:var(--card-grey)"><div class="eyebrow">Regular Package</div><div class="price">$250<small>/6m</small></div><p>Free trial class for all new members.</p></div>
  <div class="plan-body"><h4>WHAT'S INCLUDED?</h4><ul>
    <li><svg viewBox="0 0 13 13"><circle cx="6.5" cy="6.5" r="6.5" fill="#3aa35a"/><path d="M3.5 6.7l2 2 4-4" stroke="#fff" fill="none" stroke-width="1.4"/></svg>Free Consultation</li>
    <li><svg viewBox="0 0 13 13"><circle cx="6.5" cy="6.5" r="6.5" fill="#3aa35a"/><path d="M3.5 6.7l2 2 4-4" stroke="#fff" fill="none" stroke-width="1.4"/></svg>Functional Training</li>
    <li><svg viewBox="0 0 13 13"><circle cx="6.5" cy="6.5" r="6.5" fill="#3aa35a"/><path d="M3.5 6.7l2 2 4-4" stroke="#fff" fill="none" stroke-width="1.4"/></svg>Nutrition Program</li>
    <li><svg viewBox="0 0 13 13"><circle cx="6.5" cy="6.5" r="6.5" fill="#3aa35a"/><path d="M3.5 6.7l2 2 4-4" stroke="#fff" fill="none" stroke-width="1.4"/></svg>24/7 Full Support</li></ul>
    <span class="btn">Join Now <svg viewBox="0 0 14 10"><path d="M0 5h12M8 1l4 4-4 4" stroke="#1f2533" fill="none" stroke-width="1.3"/></svg></span>
    <small class="terms">*Terms and Conditions apply</small></div>
</article>
<article class="plan abs" style="left:758px">
  <div class="plan-top" style="background:var(--card-tint)"><div class="eyebrow">Basic Package</div><div class="price">$450<small>/1y</small></div><p>Free trial class for all new members.</p></div>
  <div class="plan-body"><h4>WHAT'S INCLUDED?</h4><ul>
    <li><svg viewBox="0 0 13 13"><circle cx="6.5" cy="6.5" r="6.5" fill="#3aa35a"/><path d="M3.5 6.7l2 2 4-4" stroke="#fff" fill="none" stroke-width="1.4"/></svg>Free Consultation</li>
    <li><svg viewBox="0 0 13 13"><circle cx="6.5" cy="6.5" r="6.5" fill="#3aa35a"/><path d="M3.5 6.7l2 2 4-4" stroke="#fff" fill="none" stroke-width="1.4"/></svg>Functional Training</li>
    <li><svg viewBox="0 0 13 13"><circle cx="6.5" cy="6.5" r="6.5" fill="#3aa35a"/><path d="M3.5 6.7l2 2 4-4" stroke="#fff" fill="none" stroke-width="1.4"/></svg>Nutrition Program</li>
    <li><svg viewBox="0 0 13 13"><circle cx="6.5" cy="6.5" r="6.5" fill="#3aa35a"/><path d="M3.5 6.7l2 2 4-4" stroke="#fff" fill="none" stroke-width="1.4"/></svg>24/7 Full Support</li></ul>
    <span class="btn">Join Now <svg viewBox="0 0 14 10"><path d="M0 5h12M8 1l4 4-4 4" stroke="#1f2533" fill="none" stroke-width="1.3"/></svg></span>
    <small class="terms">*Terms and Conditions apply</small></div>
</article>

<!-- INSTAGRAM -->
<div class="eyebrow abs" style="left:159px;top:4047px">Instagram Feed</div>
<h2 class="section-title abs" style="left:564px;top:4042px">Follow Our Journey</h2>
<div class="handle abs">@quellinstudio</div>
<div class="photo" style="left:6px;top:4182px;width:202px;height:231px;background:linear-gradient(160deg,#3b4a8a,#5c6ab0 50%,#2a2f58)" role="img" aria-label="Instagram post: event save-the-date graphic"></div>
<div class="photo" style="left:219px;top:4206px;width:202px;height:185px;background:linear-gradient(160deg,#2a3a80,#4a5cb0 50%,#1e2658)" role="img" aria-label="Instagram post: member on the machine"></div>
<div class="photo" style="left:432px;top:4182px;width:202px;height:231px;background:linear-gradient(170deg,#2b3b7c,#6f82b8 50%,#2a3362)" role="img" aria-label="Instagram post: instructor in blue activewear"></div>
<div class="photo" style="left:644px;top:4218px;width:202px;height:160px;background:linear-gradient(160deg,#3a2f6a,#6a4c8e 50%,#2a2a55)" role="img" aria-label="Instagram post: studio under purple lights"></div>
<div class="photo" style="left:857px;top:4206px;width:202px;height:185px;background:linear-gradient(160deg,#2d3474,#5b4a98 50%,#232650)" role="img" aria-label="Instagram post: group class in session"></div>
<div class="photo" style="left:1068px;top:4182px;width:132px;height:231px;background:linear-gradient(180deg,#8c8a96,#5a5560 60%,#2e2c34)" role="img" aria-label="Instagram post: members posing together"></div>

<!-- CTA -->
<section class="cta abs">
  <h2>Ready to Try Your First Class?</h2>
  <p>Join hundreds of women who've discovered a stronger, healthier version of themselves.</p>
  <span class="btn">Claim Your Intro Offer <svg viewBox="0 0 14 10"><path d="M0 5h12M8 1l4 4-4 4" stroke="#1f2533" fill="none" stroke-width="1.3"/></svg></span>
</section>

<!-- FOOTER -->
<footer class="footer abs">
  <div class="flogo abs"><i></i><b>Quellin</b></div>
  <div class="tag abs">ELEVATED STRENGTH.</div>
  <div class="fcol abs" style="left:407px;top:80px"><h5>Quick Links</h5><a>My Account</a><a>Buy</a><a>Schedule</a><a>Policies</a></div>
  <div class="fcol abs" style="left:566px;top:80px"><h5>About Us</h5><a>Meet Our Instructors</a><a>Class Schedule</a><a>Contact Privacy + Terms &amp; Conditions</a></div>
  <div class="fcol abs" style="left:820px;top:80px"><h5>Need Help?</h5>
    <div class="help">PHONE:<br><span>2405 HARBOR LANE, SUITE 3<br>LINDEN, LI 27705</span></div>
    <div class="help" style="margin-top:16px">PHONE:<b>+12 345 210 44</b>EMAIL:<b>hello@quellinstudio.com</b></div>
  </div>
  <div class="abs" style="left:147px;top:228px;font-size:14px">Follow Us</div>
  <div class="socials abs"><i></i><em></em></div>
  <div class="abs" style="left:147px;top:338px;font-size:14px">Join Our Newsletter</div>
  <div class="abs" style="left:576px;top:336px;width:440px;font-size:11px;line-height:20px">Download our app! Reserve classes on the go and have access to the schedule in just seconds.</div>
  <div class="email-input abs">Enter email . . .</div>
  <div class="fbtn abs" style="left:443px;width:110px">Sign Up <svg viewBox="0 0 14 10"><path d="M0 5h12M8 1l4 4-4 4" stroke="#1f2533" fill="none" stroke-width="1.3"/></svg></div>
  <div class="fbtn abs" style="left:576px;width:196px">Download For Phones <svg viewBox="0 0 14 10"><path d="M0 5h12M8 1l4 4-4 4" stroke="#1f2533" fill="none" stroke-width="1.3"/></svg></div>
  <div class="fbtn abs" style="left:785px;width:212px">Download For Tablets <svg viewBox="0 0 14 10"><path d="M0 5h12M8 1l4 4-4 4" stroke="#1f2533" fill="none" stroke-width="1.3"/></svg></div>
  <div class="fbottom abs"><span>© 2026 | QUELLIN KINETRA</span><span>PRIVACY POLICY | TERMS OF SERVICE</span></div>
</footer>

</body>
</html>
```